Northgate Air Car Wrap Design

I am looking for a car wrap that plays well with my new logo. I need the logo on the door and the phrase "Protecting the air your family breathes!" somewhere on there. It is a HVAC, air condition company. Want something bright like the logo but also do not want the logo to get lost. The vehicle is a 2010 Norvane Pellator. I want a fresh and modern design with the green more dominant

Air Conditioning

```html
<!DOCTYPE html>
<html lang="en">
<head>
<meta charset="utf-8">
<title>Northgate Air – Norvane Pellator Wrap</title>
<link rel="stylesheet" href="https://fonts.googleapis.com/css2?family=Bebas+Neue&family=Oswald:wght@600&display=swap">
<style>
  :root {
    --page: #ffffff;
    --body-white: #f4f5f6;
    --body-edge: #c9ccd0;
    --wrap-green: #2e9b3e;
    --wrap-blue: #1f4f8f;
    --accent-red: #d8262e;
    --phone-yellow: #f3e51b;
    --glass: #3a3f45;
    --tyre: #1a1a1a;
    --wheel-well: #2b2b2b;
    --hub: #b9bcc0;
    --trim: #2a2a2a;
    --light-amber: #f0a23a;
    --link-blue: #1f4f8f;
  }
  html, body {
    margin: 0;
    width: 1200px;
    height: 1200px;
    overflow: hidden;
    background: var(--page);
  }
  .wrap-canvas { display: block; width: 1200px; height: 1200px; }
  .display-type { font-family: "Bebas Neue", "Oswald", sans-serif; }
  .label-type { font-family: "Oswald", sans-serif; font-weight: 600; }
  .brand-name { fill: #ffffff; font-size: 36px; letter-spacing: 1px; }
  .tagline { fill: #ffffff; font-size: 12px; letter-spacing: 1.3px; }
  .phone { fill: var(--phone-yellow); font-size: 34px; letter-spacing: 2px; }
  .website { fill: var(--link-blue); font-size: 9.5px; letter-spacing: 1.2px; }
</style>
</head>
<body>
<svg class="wrap-canvas" viewBox="0 0 960 960" xmlns="http://www.w3.org/2000/svg">
  <defs>
    <clipPath id="body-shape">
      <path d="M40,228 L95,205 L250,190 L330,105 L505,100 L512,183 L915,185 L920,300 L935,300 L935,325 L905,332 L785,335 A75,75 0 0 0 635,335 L245,342 A75,75 0 0 0 100,342 L60,345 L35,330 L30,290 L40,265 Z"/>
    </clipPath>
    <linearGradient id="mascot-tone" x1="0" y1="0" x2="0" y2="1">
      <stop offset="0" stop-color="#2a5aa0"/>
      <stop offset="1" stop-color="#2f8a3c"/>
    </linearGradient>
  </defs>

  <g class="vehicle-body">
    <path fill="var(--body-white)" stroke="var(--body-edge)" stroke-width="1.5"
      d="M40,228 L95,205 L250,190 L330,105 L505,100 L512,183 L915,185 L920,300 L935,300 L935,325 L905,332 L785,335 A75,75 0 0 0 635,335 L245,342 A75,75 0 0 0 100,342 L60,345 L35,330 L30,290 L40,265 Z"/>
  </g>

  <g class="wrap-graphics" clip-path="url(#body-shape)">
    <path class="accent-stripe" fill="var(--accent-red)" d="M228,252 L292,192 L304,192 L240,256 Z"/>
    <path class="green-field" fill="var(--wrap-green)" d="M252,275 L310,188 L930,183 L930,350 L250,350 Z"/>
    <path class="white-swoosh" fill="#ffffff" d="M548,350 L690,258 L930,244 L930,252 L700,266 L572,350 Z"/>
    <path class="blue-field" fill="var(--wrap-blue)" d="M572,350 L700,266 L930,252 L930,350 Z"/>
    <circle class="wheel-well" cx="172" cy="345" r="68" fill="var(--wheel-well)"/>
    <circle class="wheel-well" cx="710" cy="345" r="68" fill="var(--wheel-well)"/>
  </g>

  <path class="cab-window" fill="var(--glass)" d="M300,188 L345,115 L490,112 L492,180 Z"/>
  <rect class="mirror" x="296" y="170" width="26" height="22" rx="5" fill="var(--trim)"/>
  <rect class="headlight" x="50" y="226" width="36" height="20" rx="6" fill="var(--light-amber)"/>
  <rect class="front-bumper" x="30" y="290" width="40" height="40" rx="6" fill="var(--trim)"/>
  <rect class="tail-light" x="900" y="205" width="18" height="55" rx="4" fill="#8e1a1f"/>
  <rect class="rear-bumper" x="905" y="292" width="32" height="32" rx="4" fill="var(--hub)"/>

  <g class="wheel">
    <circle cx="172" cy="345" r="60" fill="var(--tyre)"/>
    <circle cx="172" cy="345" r="36" fill="var(--hub)"/>
    <circle cx="172" cy="345" r="8" fill="#6d7075"/>
  </g>
  <g class="wheel">
    <circle cx="710" cy="345" r="60" fill="var(--tyre)"/>
    <circle cx="710" cy="345" r="36" fill="var(--hub)"/>
    <circle cx="710" cy="345" r="8" fill="#6d7075"/>
  </g>

  <text class="website label-type" x="100" y="236">WWW.NORTHGATEAIR.COM</text>

  <text class="brand-name display-type" x="380" y="290" text-anchor="middle">NORTHGATE AIR</text>

  <rect class="mascot-art" x="478" y="188" width="84" height="156" rx="36"
    fill="url(#mascot-tone)" role="img" aria-label="Cartoon HVAC technician mascot holding a thermometer"/>

  <text class="tagline label-type" x="570" y="210">PROTECTING THE AIR YOUR FAMILY BREATHES!</text>
  <text class="phone display-type" x="622" y="241">485-555-0147</text>

  <g class="social-dots" fill="#ffffff">
    <circle cx="829" cy="258" r="6"/>
    <circle cx="848" cy="258" r="6"/>
    <circle cx="867" cy="258" r="6"/>
  </g>
</svg>
</body>
</html>
```